Corvelle Strategies business card

I need a business card for my new strategic consulting LLC, Corvelle Strategies. We specialize in helping people who care about broadband technology and telecommunications policy, and we're based in Washington DC. I'm looking for a card that says smart, credible, future-facing and signals a high level of expertise. It's DC, so there's clearly a limit to how crazy we can go with this card, but I am looking for a design that reflects a company that is comfortable with technology, policy, and having a little bit fun. I'm uploading my logo below, and I'd like to have it be part of the card design in some fashion.
Target Market(s)
Telecommunications and technology policy professionals
Industry/Entity Type
Technology policy
Contact Information for Business Card
Name of business, my name (Glen Mosswater), email (glen@corvellestrategies-example.com) , phone number (202-555-0148)phone number

```html
<!DOCTYPE html>
<html lang="en">
<head>
<meta charset="UTF-8">
<title>Corvelle Strategies – Business Card</title>
<link rel="stylesheet" href="https://fonts.googleapis.com/css2?family=Montserrat:wght@400;600;700&display=swap">
<style>
  :root {
    --brand-blue: #0a4f9e;
    --brand-orange: #f7b03c;
    --card-white: #ffffff;
    --ink: #1d1d1f;
    --backdrop: #3a3a3a;
  }
  * { margin: 0; padding: 0; box-sizing: border-box; }
  html, body { width: 1200px; height: 875px; overflow: hidden; }
  body {
    background: var(--backdrop);
    font-family: "Montserrat", Arial, sans-serif;
    display: flex;
    flex-direction: column;
    align-items: center;
    justify-content: center;
    gap: 40px;
  }
  .card {
    position: relative;
    width: 640px;
    height: 366px;
    background: var(--card-white);
    border-radius: 22px;
    border-bottom: 4px solid var(--brand-orange);
    overflow: hidden;
    box-shadow: 0 14px 30px rgba(0,0,0,0.35);
  }
  .brand {
    display: flex;
    align-items: center;
    gap: 14px;
    color: var(--brand-blue);
    font-weight: 700;
    white-space: nowrap;
  }
  .brand-dot {
    width: 26px; height: 26px;
    border-radius: 50%;
    background: var(--brand-orange);
    flex: none;
  }
  .card-front { display: flex; align-items: center; justify-content: center; }
  .card-front .brand { font-size: 44px; }
  .card-back .brand {
    position: absolute;
    top: 70px; left: 60px;
    font-size: 40px;
  }
  .card-back .brand-dot { width: 24px; height: 24px; }
  .back-swoosh { position: absolute; left: 0; bottom: 0; width: 640px; height: 140px; }
  .holder-name {
    position: absolute;
    left: 60px; top: 196px;
    font-size: 26px;
    font-weight: 700;
    color: var(--brand-blue);
  }
  .divider {
    position: absolute;
    left: 330px; top: 172px;
    width: 1.5px; height: 62px;
    background: var(--brand-blue);
  }
  .contact-list {
    position: absolute;
    left: 352px; top: 176px;
    list-style: none;
    font-size: 12.5px;
    color: var(--ink);
    display: flex; flex-direction: column; gap: 12px;
  }
  .contact-list li { display: flex; align-items: center; gap: 8px; }
  .contact-list svg { width: 14px; height: 14px; fill: var(--brand-blue); flex: none; }
</style>
</head>
<body>

  <section class="card card-front" aria-label="Card front">
    <div class="brand"><span class="brand-dot"></span>Corvelle Strategies</div>
  </section>

  <section class="card card-back" aria-label="Card back">
    <div class="brand"><span class="brand-dot"></span>Corvelle Strategies</div>

    <p class="holder-name">Glen Mosswater</p>
    <span class="divider"></span>
    <ul class="contact-list">
      <li>
        <svg viewBox="0 0 24 24" aria-hidden="true"><path d="M6.6 10.8a15.1 15.1 0 0 0 6.6 6.6l2.2-2.2c.3-.3.7-.4 1-.2 1.1.4 2.3.6 3.6.6.6 0 1 .4 1 1V20c0 .6-.4 1-1 1A17 17 0 0 1 3 4c0-.6.4-1 1-1h3.5c.6 0 1 .4 1 1 0 1.3.2 2.5.6 3.6.1.3 0 .7-.2 1z"/></svg>
        202-555-0148
      </li>
      <li>
        <svg viewBox="0 0 24 24" aria-hidden="true"><path d="M2 5h20v14H2zm2 2v.5l8 5 8-5V7zm0 2.8V17h16V9.8l-8 5z"/></svg>
        corvellestrategies-example.com
      </li>
    </ul>

    <svg class="back-swoosh" viewBox="0 0 640 140" preserveAspectRatio="none" aria-hidden="true">
      <path d="M0 128 C 200 100, 420 70, 640 0 L 640 14 C 430 84, 220 116, 0 134 Z" fill="var(--brand-orange)"/>
      <path d="M0 112 C 210 104, 430 70, 640 20 L 640 140 L 0 140 Z" fill="var(--brand-blue)"/>
    </svg>
  </section>

</body>
</html>
```